Plumber referral program cards

We're a busy Restoration company servicing residential and commercial properties damaged by water fire and mold. We hold the standard for Excellence, Integrity and Reliability.
This business card needs to be designed to generate high quality plumbing leads through water damage referrals

FRONT: (no specific chronological order)
-Water Damage Referral program for plumbers
-We pay plumbers $800 CASH on each water damage referral everyday!
-"To us, business is personal. Which is why referrals means rewards."
-Refer and Earn• Paid same day!

- Your customer will ALWAYS receive a FREE evaluation.
Rapid Response
24 hours a day/7 days a week

BACK: (no specific chronological order)
Water extraction•plumbing leaks•slab leaks•
Sub floor drying and repairs•Sewage cleanup•supply line rupture •structural drying•overflows•mold remediation•

-Call Wet Gone next time you run into a water damage!
555-7-WET-GON

Summit Pipefitter Bonus Scheme Bonuses
-Just to show how much your referrals mean to us, Receive $100 on every referral sent, No matter what!
- Refer Wet Gone to other property service professionals, and you recieve $100 cash for every job THEY send us!

Contact us for more information
RB Morwenna
Water Damage Restoration Specialist
Phone: 555-7-WETGON
Email: Rmorwenna@ringwetgon.example
Website: www.ringwetgon.example

Target Market(s)

Plumbers

Industry/Entity Type

It Company

Contact Information for Business Card

Rapid Response

555-7-WET-GON

RB Morwenna
Phone: 555-7-WETGON

Font styles to use
Other font styles liked:
• Times etc

Colors

Designer to choose colors to be used in the design.

Requirements
Must have
• Emphasized $800 referral fee
• Eye catching & appealing
• Our company logo and color matching
• Attached files of example competitors ads

```html
<!DOCTYPE html>
<html lang="en">
<head>
<meta charset="utf-8">
<title>Wet Gone – Plumber Referral Cards</title>
<link href="https://fonts.googleapis.com/css2?family=PT+Sans:wght@400;700&display=swap" rel="stylesheet">
<style>
  :root {
    --red: #e0333f;
    --blue: #1d4c9e;
    --ink: #1f1f24;
    --paper: #f7f8fb;
    --paper-tint: #dfe3ee;
    --stage: #e9e9e7;
  }
  * { box-sizing: border-box; margin: 0; padding: 0; }
  html, body { width: 1200px; height: 800px; overflow: hidden; }
  body {
    background: var(--stage);
    font-family: "PT Sans", Arial, sans-serif;
    color: var(--ink);
    display: flex;
    align-items: center;
    justify-content: center;
    gap: 40px;
  }
  .card {
    position: relative;
    width: 560px;
    height: 320px;
    overflow: hidden;
    background: linear-gradient(135deg, var(--paper) 35%, var(--paper-tint) 100%);
    box-shadow: 0 6px 18px rgba(0,0,0,.15);
  }
  .card__bands { position: absolute; inset: 0; width: 100%; height: 100%; }
  .card__texture {
    position: absolute;
    right: 0; top: 0;
    width: 55%; height: 100%;
    background: linear-gradient(160deg, rgba(205,212,230,.55), rgba(255,255,255,0));
  }
  .brand { display: flex; align-items: center; gap: 10px; }
  .brand__dot {
    width: 30px; height: 30px; border-radius: 50%;
    background: var(--blue);
  }
  .brand__name {
    font-size: 42px; font-weight: 700; line-height: 1;
    color: var(--ink);
    letter-spacing: .5px;
  }
  .accent { color: var(--red); font-weight: 700; }

  /* Front */
  .front .brand { position: absolute; left: 36px; top: 48px; }
  .front__copy {
    position: absolute; left: 36px; top: 112px;
    font-size: 15px; line-height: 1.42;
  }

  /* Back */
  .back .brand { position: absolute; left: 300px; top: 26px; }
  .back .brand__name { font-size: 32px; }
  .back .brand__dot { width: 22px; height: 22px; }
  .contact { position: absolute; left: 300px; top: 70px; }
  .contact__name { font-size: 22px; color: var(--red); line-height: 1.1; }
  .contact__role { font-size: 11px; margin-bottom: 4px; }
  .contact__line { display: flex; align-items: center; gap: 6px; font-size: 14px; line-height: 1.35; }
  .contact__line svg { width: 12px; height: 12px; fill: var(--ink); flex: none; }
  .services {
    position: absolute; left: 28px; top: 38px;
    list-style: none; font-size: 14px; line-height: 1.35;
  }
  .services li::before {
    content: ""; display: inline-block;
    width: 5px; height: 5px; border-radius: 50%;
    background: var(--blue); margin-right: 7px; vertical-align: middle;
  }
  .call-out { position: absolute; left: 28px; top: 220px; font-size: 11px; line-height: 1.3; }
  .bonus {
    position: absolute; left: 200px; top: 190px; width: 340px;
    text-align: center; font-size: 11.5px; line-height: 1.35;
  }
  .bonus__title { font-size: 14px; color: var(--red); font-weight: 700; }
</style>
</head>
<body>

  <!-- Front -->
  <section class="card front">
    <div class="card__texture" role="img" aria-label="Faint geometric square pattern"></div>
    <svg class="card__bands" viewBox="0 0 560 320" preserveAspectRatio="none" aria-hidden="true">
      <rect x="0" y="0" width="560" height="8" fill="var(--blue)"/>
      <rect x="0" y="8" width="560" height="5" fill="var(--red)"/>
      <polygon points="360,13 560,13 560,38 400,60 330,60" fill="var(--red)"/>
      <polygon points="330,60 400,60 560,38 560,70 420,92 300,92" fill="var(--blue)"/>
      <rect x="0" y="306" width="560" height="14" fill="var(--blue)"/>
    </svg>
    <div class="brand">
      <span class="brand__name">Wet Gone</span>
      <span class="brand__dot"></span>
    </div>
    <div class="front__copy">
      <p>Water Damage Referral Program For Plumbers</p>
      <p>We Pay Plumbers <span class="accent">$800</span> Cash On Each Water Damage Referral Everyday!</p>
      <p>"To Us, Business Is Personal. Which Is Why Referrals Means Rewards."</p>
      <p>Refer And Earn• Paid Same Day!</p>
      <p>Your Customer Will Always Receive A <span class="accent">Free</span> Evaluation.</p>
      <p>Rapid Response</p>
      <p>24 Hours A Day/7 Days A Week</p>
    </div>
  </section>

  <!-- Back -->
  <section class="card back">
    <div class="card__texture" role="img" aria-label="Faint geometric square pattern"></div>
    <svg class="card__bands" viewBox="0 0 560 320" preserveAspectRatio="none" aria-hidden="true">
      <polygon points="0,262 150,262 190,290 0,290" fill="var(--red)"/>
      <polygon points="0,290 190,290 220,308 0,308" fill="var(--blue)"/>
      <rect x="0" y="308" width="560" height="5" fill="var(--red)"/>
      <rect x="0" y="313" width="560" height="7" fill="var(--blue)"/>
      <rect x="548" y="0" width="5" height="320" fill="var(--red)"/>
      <rect x="553" y="0" width="7" height="320" fill="var(--blue)"/>
    </svg>

    <ul class="services">
      <li>Water Extraction</li>
      <li>Plumbing Leak</li>
      <li>Slab Leaks</li>
      <li>Sub Floor Drying And Repairs</li>
      <li>Sewage Cleanup</li>
      <li>Supply Line Rupture</li>
      <li>Structural Drying</li>
      <li>Overflows</li>
      <li>Mold Remediation</li>
    </ul>
    <p class="call-out">Call Wet Gone Next Time<br>You Run Into A Water Damage!<br>555-7-WET-GON</p>

    <div class="brand">
      <span class="brand__name">Wet Gone</span>
      <span class="brand__dot"></span>
    </div>
    <div class="contact">
      <p class="contact__name">RB Morwenna</p>
      <p class="contact__role">Water Damage Restoration Specialist</p>
      <p class="contact__line">
        <svg viewBox="0 0 24 24"><path d="M6.6 10.8a15 15 0 0 0 6.6 6.6l2.2-2.2c.3-.3.7-.4 1-.2 1.1.4 2.3.6 3.6.6.6 0 1 .4 1 1V20c0 .6-.4 1-1 1A17 17 0 0 1 3 4c0-.6.4-1 1-1h3.5c.6 0 1 .4 1 1 0 1.3.2 2.5.6 3.6.1.3 0 .7-.2 1z"/></svg>
        555-7-WETGON
      </p>
      <p class="contact__line">
        <svg viewBox="0 0 24 24"><path d="M2 5h20v14H2zm2 2v.5l8 5 8-5V7z"/></svg>
        Rmorwenna@ringwetgon.example
      </p>
      <p class="contact__line">
        <svg viewBox="0 0 24 24"><path d="M12 2a10 10 0 1 0 0 20 10 10 0 0 0 0-20zm0 2c1 0 2.3 2 2.8 5H9.2C9.7 6 11 4 12 4zM4.3 11h4.6a18 18 0 0 0 0 2H4.3a8 8 0 0 1 0-2zm6.7 0h2a16 16 0 0 1 0 2h-2a16 16 0 0 1 0-2zm4.1 0h4.6a8 8 0 0 1 0 2h-4.6a18 18 0 0 0 0-2zM9.2 15h5.6c-.5 3-1.8 5-2.8 5s-2.3-2-2.8-5z"/></svg>
        www.ringwetgon.example
      </p>
    </div>

    <div class="bonus">
      <p class="bonus__title">Summit Pipefitter Bonus Scheme Bonuses</p>
      <p>Just To Show How Much Your Referrals Mean To Us, Receive $100 On Every Referral Sent, No Matter What!</p>
      <p>Refer Wet Gone To Other Property Service Professionals, And You Recieve $100 Cash For Every Job They Send Us!</p>
    </div>
  </section>

</body>
</html>
```